Creation of a Velunta website

Velunta is a company% 26 # 233; t% 26 # 233; consulting that accompanies Swiss companies or% 26 # 233; strang% 26 # 232; res in the d% 26 # 233; development of their business on the market% 26 # 233; Switzerland by providing strategic contacts (personalized contact program% 26 # 233; s) or market information% 26 # 233; (% 26 # 233; market research% 26 # 233;) and by providing administrative support (repr% 26 # 233; tax representation) or logistics (organization of% 26 # 233; v% 26 # 233; nement, assistance for participation% 26 # 224; fairs). Our customers are mainly European companies wishing to develop their business in Switzerland. N% 26 # 233; however, our services are% 26 # 233; also aimed at Swiss companies wishing to develop in other parts of Switzerland. Our site must therefore be% 26 # 234; capable of being translated into several languages. The services offered% 26 # 233; s by Velunta may also% 26 # 233; also% 26 # 39;% 26 # 233; tender% 26 # 224; promoting tourism in Switzerland for countries or regions% 26 # 233; foreigners or% 26 # 224; the promotion of trade fairs or fairs with% 26 # 232; sd% 26 # 39; companies of the sectors concerned% 26 # 233; s. It is therefore n% 26 # 233; necessary to be able to add sub-headings of services which can% 26 # 234; be displayed% 26 # 233; es or hide% 26 # 233; es as required. We are 2 associates% 26 # 233; s, low% 26 # 233; s in the French-speaking parts (Neuch% 26 # 226; tel) and al% 26 # 233; manique (Zurich) of Switzerland.

Target Market(s)

Swiss or European companies wishing to develop their activities in Switzerland.

Coding

Coded - Design and coding required

Colors

Designer to choose colors to be used in the design.

Requirements
Must have
• A home page A section of% 26 # 233; writing the services offered% 26 # 233; es by Velunta with the possibility% 26 # 233; d% 26 # 39; add sub-headings which can% 26 # 234; be displayed% 26 # 233; e or hidden% 26 # 233; e A page with the r% 26 # 233; f% 26 # 233; which can be displayed% 26 # 233; e or hidden% 26 # 233; e A page of% 26 # 233; writing l% 26 # 39;% 26 # 233; team A page with form contact, addresses and int card% 26 # 233; gr% 26 # 233; e The site must% 26 # 234; be low% 26 # 233; on a CMS allowing% 26 # 39;% 26 # 234; to be autonomous in modifying the website The possibility% 26 # 233; to be able to translate the site into several languages (FR, EN, DE, IT, NL, ...)

```html
<!DOCTYPE html>
<html lang="en">
<head>
<meta charset="utf-8">
<title>Velunta – Market Research and Logistics</title>
<link href="https://fonts.googleapis.com/css2?family=Exo+2:wght@300;400;600;700&family=Lato:wght@400;700&family=Michroma&display=swap" rel="stylesheet">
<style>
:root{
  --navy:#1e3d58;
  --navy-deep:#16314a;
  --steel:#3d5d76;
  --mist:#b3bfcc;
  --mist-light:#dde2e8;
  --ink:#2a4a64;
  --text:#4a5560;
  --client:#6a6f75;
  --white:#ffffff;
}
*{margin:0;padding:0;box-sizing:border-box}
html,body{width:1200px;height:3413px;overflow:hidden;background:var(--white)}
body{position:relative;font-family:"Lato",sans-serif;color:var(--text)}
.abs{position:absolute}
.center{left:0;width:1200px;text-align:center}

/* header */
.site-header{position:absolute;left:0;top:0;width:1200px;height:90px;background:var(--white)}
.brand-mark{left:102px;top:24px;width:42px;height:42px;border-radius:9px;background:var(--navy)}
.brand-name{left:167px;top:24px;font-family:"Exo 2",sans-serif;font-weight:300;font-size:38px;letter-spacing:3px;color:var(--navy);line-height:42px}
.main-nav a{position:absolute;top:35px;font-family:"Lato",sans-serif;font-size:15px;color:var(--steel);text-decoration:none;transform:translateX(-50%);white-space:nowrap}
.main-nav a.active{color:var(--navy);font-weight:700}
.main-nav .underline{position:absolute;top:63px;width:46px;height:2px;background:var(--navy);transform:translateX(-50%)}

/* hero */
.hero{left:0;top:90px;width:1200px;height:672px}
.hero-text{top:300px;color:var(--white);font-family:"Exo 2",sans-serif}
.hero-kicker{font-weight:300;font-size:28px;letter-spacing:1px}
.hero-title{font-weight:700;font-size:58px;line-height:62px;margin-top:10px}
.hero-title span{display:block;font-weight:300}

/* about */
.about-visual{left:166px;top:817px;width:377px;height:378px;border-radius:110px;background:linear-gradient(135deg,#8a7e70,#c9c2b8 55%,#6f6253)}
.section-title{font-family:"Exo 2",sans-serif;font-weight:700;font-size:33px;color:var(--navy)}
.about-title{left:593px;top:840px}
.about-copy{left:595px;top:908px;width:500px;font-size:18px;line-height:25px;color:var(--text)}
.about-copy p+p{margin-top:29px}
.btn-leaf{left:599px;top:1120px;width:180px;height:52px;background:var(--navy);color:var(--white);border-radius:22px 4px 22px 4px;font-size:16px;font-weight:700;line-height:52px;text-align:center;letter-spacing:.5px}

/* services */
.services{left:0;top:1274px;width:1200px;height:551px;background:linear-gradient(180deg,#e4e7eb,#d6dce2 60%,#e6e9ed)}
.services-title{top:1328px}
.service{position:absolute;text-align:center;font-family:"Lato",sans-serif}
.service h3{font-family:"Exo 2",sans-serif;font-weight:600;font-size:19px;color:var(--white);letter-spacing:.3px}
.service p{font-size:12.5px;line-height:19px;color:#eef1f4;margin-top:8px}

/* team */
.team{left:0;top:1825px;width:1200px;height:502px;background:var(--navy)}
.team-title{top:1858px;color:var(--white)}
.team-intro{top:1910px;font-size:13px;color:var(--white)}
.member{position:absolute;top:1971px;width:200px;text-align:center;transform:translateX(-50%)}
.member-photo{width:164px;height:164px;border-radius:50%;margin:0 auto;background:radial-gradient(circle at 50% 45%,#b68d74,#8a6e5e 60%,#d9d6d2)}
.member h4{font-family:"Michroma",sans-serif;font-weight:400;font-size:12.5px;color:var(--white);margin-top:18px;letter-spacing:.5px}
.member p{font-size:12px;line-height:17px;color:#dce4eb;margin-top:10px}
.btn-outline{display:inline-block;margin-top:15px;width:102px;height:36px;border:1.5px solid var(--white);font-family:"Michroma",sans-serif;font-size:12px;line-height:33px;color:var(--white)}

/* clients */
.clients-title{top:2386px}
.client{position:absolute;top:2490px;font-family:"Lato",sans-serif;font-weight:700;font-size:20px;color:var(--client);transform:translateX(-50%);white-space:nowrap;display:flex;align-items:center;gap:8px}
.client .dot{width:14px;height:14px;border-radius:50%;background:#8a9097}

/* contact */
.contact{left:0;top:2690px;width:1200px;height:723px;background:linear-gradient(180deg,#2b4960,#1f3e57 55%,#1a3650)}
.contact-title{left:163px;top:2794px;color:var(--white);font-size:31px}
.contact-item{position:absolute;left:229px;color:var(--white)}
.contact-item h5{font-family:"Lato",sans-serif;font-weight:700;font-size:17px;text-transform:uppercase;letter-spacing:.3px}
.contact-item div{font-size:17px;margin-top:3px}
.field{position:absolute;left:621px;width:466px;height:42px;border:1.5px solid #d7dee5;color:var(--white);font-size:16px;padding:9px 21px}
.btn-submit{left:625px;top:3061px;width:180px;height:50px;background:var(--mist);color:var(--navy);border-radius:22px 4px 22px 4px;font-weight:700;font-size:16px;line-height:50px;text-align:center}

/* footer */
.footer-nav a{position:absolute;top:3272px;font-size:16px;color:var(--navy);font-weight:700;text-decoration:none;transform:translateX(-50%);white-space:nowrap}
.copyright{top:3304px;font-size:13px;color:#7b8a98}
.social{position:absolute;top:3336px;width:36px;height:36px;border-radius:50%;background:var(--navy)}
</style>
</head>
<body>

<header class="site-header">
  <div class="abs brand-mark"></div>
  <div class="abs brand-name">VELUNTA</div>
  <nav class="main-nav">
    <a href="#" class="active" style="left:510px">HOME</a>
    <a href="#" style="left:608px">ABOUT US</a>
    <a href="#" style="left:735px">OUR SERVICES</a>
    <a href="#" style="left:845px">TEAM</a>
    <a href="#" style="left:940px">CONTACT</a>
    <a href="#" style="left:1030px;color:var(--navy);font-weight:700">EN ⌄</a>
    <span class="underline" style="left:510px"></span>
  </nav>
</header>

<svg class="abs hero" viewBox="0 0 1200 672" role="img" aria-label="Snowy mountain range above a lake, tinted in steel blue">
  <defs>
    <linearGradient id="heroTone" x1="0" y1="0" x2="0" y2="1">
      <stop offset="0" stop-color="#4a6b84"/>
      <stop offset=".45" stop-color="#5f7d94"/>
      <stop offset=".7" stop-color="#2f5069"/>
      <stop offset="1" stop-color="#1f3e57"/>
    </linearGradient>
  </defs>
  <path d="M0 0H1200V562L640 666Q600 674 560 666L0 562Z" fill="url(#heroTone)"/>
  <path d="M96 262L74 286L96 310" fill="none" stroke="#fff" stroke-width="2"/>
  <path d="M1108 262L1130 286L1108 310" fill="none" stroke="#fff" stroke-width="2"/>
</svg>
<div class="abs center hero-text">
  <div class="hero-kicker">WELCOME TO VELUNTA</div>
  <h1 class="hero-title">MARKET RESEARCH<span>AND LOGISTICS</span></h1>
</div>

<div class="abs about-visual" role="img" aria-label="Desk seen from above with charts, sticky notes and a laptop"></div>
<h2 class="abs section-title about-title">ABOUT VELUNTA</h2>
<div class="abs about-copy">
  <p>Pellentesque faucibus Ut accumsan ultricies elit Maecenas at justo id velit placerat molestie Donec dictum lectus non odio Cras a ante vitae enim iaculis aliquam</p>
  <p>Mauris nunc quam venenatis nec euismod sit amet egestas placerat est Pellentesque habitant morbi tristique senectus et netus et malesuada fames ac turpis egestas Cras id elit</p>
</div>
<div class="abs btn-leaf">LEARN MORE</div>

<div class="abs services" role="img" aria-label="Faded photo of colleagues in a meeting"></div>
<h2 class="abs center section-title services-title">OUR SERVICES</h2>
<svg class="abs" style="left:0;top:1274px" width="1200" height="551" viewBox="0 1274 1200 551" aria-hidden="true">
  <rect x="148" y="1459" width="220" height="220" rx="62" fill="var(--mist)" transform="rotate(45 258 1569)"/>
  <rect x="473" y="1441" width="253" height="253" rx="70" fill="var(--navy)" transform="rotate(45 599 1567)"/>
  <rect x="830" y="1457" width="220" height="220" rx="62" fill="var(--mist)" transform="rotate(45 940 1567)"/>
  <g fill="none" stroke="#fff" stroke-width="1.8" stroke-linecap="round">
    <circle cx="258" cy="1516" r="24"/>
    <circle cx="258" cy="1516" r="14"/>
    <path d="M252 1522v-6M258 1522v-10M264 1522v-8M236 1544h44"/>
    <path d="M258 1674v24M248 1688l10 10 10-10"/>
    <path d="M599 1488l10 6v12l-10 6-10-6v-12z M589 1494l10 6 10-6 M599 1500v12"/>
    <path d="M599 1470v12M599 1518v12M573 1500h12M613 1500h12M581 1482l7 7M617 1482l-7 7M581 1518l7-7M617 1518l-7-7"/>
    <path d="M599 1662v24M589 1676l10 10 10-10"/>
    <circle cx="940" cy="1512" r="28"/>
    <path d="M940 1484v56M912 1512h28M948 1500l10 24"/>
    <path d="M940 1672v24M930 1686l10 10 10-10"/>
  </g>
  <text x="927" y="1507" font-family="Lato,sans-serif" font-size="10" fill="#fff" text-anchor="middle">TAX</text>
  <text x="932" y="1531" font-family="Lato,sans-serif" font-size="13" fill="#fff" text-anchor="middle">$</text>
</svg>
<div class="service" style="left:148px;top:1562px;width:220px">
  <h3>MARKET RESEARCH</h3>
  <p>Suspendisse quam leo molestie<br>sed luctus quis feugiat in</p>
</div>
<div class="service" style="left:459px;top:1552px;width:280px">
  <h3>LOGISTICS</h3>
  <p>Allamcorper est eget tempor cursus neque<br>mi consectetuer mi a ultricies massa est<br>sed nisl Class aptent taciti</p>
</div>
<div class="service" style="left:830px;top:1560px;width:220px">
  <h3>TAX REPRESENTATION</h3>
  <p>Suspendisse quam leo molestie<br>sed luctus quis feugiat in</p>
</div>

<section class="abs team"></section>
<h2 class="abs center section-title team-title">OUR TEAM</h2>
<p class="abs center team-intro">Sed ut perspiciatis unde omnis iste natus error sit voluptatem accusantium doloremque laudantium</p>
<div class="member" style="left:264px"><div class="member-photo" role="img" aria-label="Portrait of a team member"></div><h4>JOEL MARTEN</h4><p>Sed ut perspiciatis unde iste<br>natus error sit</p><span class="btn-outline">VIEW BIO</span></div>
<div class="member" style="left:489px"><div class="member-photo" role="img" aria-label="Portrait of a team member"></div><h4>JOEL MARTEN</h4><p>Sed ut perspiciatis unde iste<br>natus error sit</p><span class="btn-outline">VIEW BIO</span></div>
<div class="member" style="left:714px"><div class="member-photo" role="img" aria-label="Portrait of a team member"></div><h4>JOEL MARTEN</h4><p>Sed ut perspiciatis unde iste<br>natus error sit</p><span class="btn-outline">VIEW BIO</span></div>
<div class="member" style="left:939px"><div class="member-photo" role="img" aria-label="Portrait of a team member"></div><h4>JOEL MARTEN</h4><p>Sed ut perspiciatis unde iste<br>natus error sit</p><span class="btn-outline">VIEW BIO</span></div>

<h2 class="abs center section-title clients-title">OUR CLIENTS</h2>
<svg class="abs" style="left:80px;top:2492px" width="1030" height="30" viewBox="0 0 1030 30" aria-hidden="true">
  <g fill="none" stroke="var(--navy)" stroke-width="2.4" stroke-linecap="round">
    <path d="M10 13h18M17 6l-7 7 7 7"/>
    <path d="M1000 13h18M1011 6l7 7-7 7"/>
  </g>
</svg>
<div class="client" style="left:229px">Brennvale</div>
<div class="client" style="left:396px">Falkor</div>
<div class="client" style="left:579px">Tandem Trust</div>
<div class="client" style="left:780px"><span class="dot" style="border-radius:2px"></span>Ardent Meridian</div>
<div class="client" style="left:968px"><span class="dot"></span>Cateryl</div>
<svg class="abs" style="left:580px;top:2589px" width="40" height="16" viewBox="0 0 40 16" aria-hidden="true">
  <circle cx="6" cy="8" r="3" fill="var(--navy)"/><circle cx="20" cy="8" r="6" fill="var(--navy)"/><circle cx="34" cy="8" r="3" fill="var(--navy)"/>
</svg>

<div class="abs contact" role="img" aria-label="Container port with cranes and a cargo ship at dusk, tinted in navy"></div>
<svg class="abs" style="left:0;top:3150px" width="1200" height="263" viewBox="0 3150 1200 263" aria-hidden="true">
  <path d="M0 3290L600 3200L1200 3290V3413H0Z" fill="#fff"/>
  <rect x="570" y="3157" width="48" height="48" rx="10" fill="var(--navy)" stroke="#fff" stroke-width="3"/>
</svg>
<h2 class="abs section-title contact-title">CONTACT US</h2>
<svg class="abs" style="left:160px;top:2862px" width="50" height="240" viewBox="0 0 50 240" aria-hidden="true">
  <g fill="none" stroke="#fff" stroke-width="2" stroke-linejoin="round">
    <path d="M25 36c-9-11-14-18-14-24a14 14 0 0128 0c0 6-5 13-14 24z"/><circle cx="25" cy="12" r="5"/>
    <path d="M8 38h34"/>
    <path d="M12 104c2-4 6-7 8-6l5 8c1 2-1 4-3 5 2 6 7 11 13 13 1-2 3-4 5-3l8 5c1 2-2 6-6 8-14 2-32-16-30-30z"/>
    <rect x="10" y="192" width="34" height="24"/><path d="M10 192l17 14 17-14M10 216l12-11M44 216l-12-11"/>
  </g>
</svg>
<div class="contact-item" style="top:2862px"><h5>Address</h5><div>214 E 52nd Street #4B Austin 78701 TX</div></div>
<div class="contact-item" style="top:2955px"><h5>Phone Number</h5><div>555.210.4817</div></div>
<div class="contact-item" style="top:3046px"><h5>Email Us</h5><div>info@veluntaconsult.com</div></div>
<div class="field" style="top:2803px">Name</div>
<div class="field" style="top:2854px">Email</div>
<div class="field" style="top:2903px">Phone</div>
<div class="field" style="top:2956px;height:88px">Message</div>
<div class="abs btn-submit">SUBMIT NOW</div>

<nav class="footer-nav">
  <a href="#" style="left:334px">HOME</a>
  <a href="#" style="left:442px">ABOUT US</a>
  <a href="#" style="left:583px">OUR SERVICES</a>
  <a href="#" style="left:704px">TEAM</a>
  <a href="#" style="left:808px">CONTACT</a>
</nav>
<p class="abs center copyright">© 2020 Company Name&nbsp; All right reserved</p>
<span class="social" style="left:508px" aria-label="Social network link"></span>
<span class="social" style="left:553px" aria-label="Social network link"></span>
<span class="social" style="left:598px" aria-label="Social network link"></span>

</body>
</html>
```